Brimovex business card

Based on company logo and website given , to design a business card temple. Slogan "Your furry friends deserves the best"
Color style please refer to our website

```html
<!DOCTYPE html>
<html lang="en">
<head>
<meta charset="utf-8">
<title>Brimovex business card</title>
<link href="https://fonts.googleapis.com/css2?family=Open+Sans:wght@400;700&display=swap" rel="stylesheet">
<style>
  :root {
    --olive: #bcb02b;
    --olive-deep: #a99e22;
    --olive-light: #cfc449;
    --ink: #4f4f4f;
    --paper: #ffffff;
    --backdrop: #dcdcda;
  }
  * { box-sizing: border-box; margin: 0; padding: 0; }
  html, body {
    width: 1200px; height: 801px; overflow: hidden;
    background: var(--backdrop);
    font-family: "Open Sans", Arial, sans-serif;
  }
  .stage {
    position: relative; width: 1200px; height: 801px;
    display: flex; align-items: center; justify-content: center; gap: 50px;
  }
  .card {
    position: relative; width: 525px; height: 300px;
    box-shadow: 0 6px 18px rgba(0,0,0,.18);
    overflow: hidden;
  }
  .card--front { background: var(--paper); }
  .front__brand {
    position: absolute; left: 40px; top: 92px; width: 205px;
    text-align: center;
    font-weight: 700; font-size: 44px; letter-spacing: -1px;
    color: var(--olive);
  }
  .front__divider {
    position: absolute; left: 262px; top: 52px;
    width: 1.5px; height: 132px; background: var(--olive);
  }
  .front__details {
    position: absolute; left: 282px; top: 48px;
    color: var(--ink); font-size: 13px; line-height: 1.35;
  }
  .details__name {
    color: var(--olive); font-weight: 700; font-size: 17px; letter-spacing: .3px;
  }
  .details__title { margin-bottom: 10px; }
  .details__address { margin-bottom: 10px; }
  .contact { display: flex; align-items: center; gap: 7px; }
  .contact svg { width: 10px; height: 10px; fill: var(--olive); flex: none; }
  .front__slogan {
    position: absolute; left: 0; right: 0; bottom: 34px;
    text-align: center; color: var(--ink); font-size: 14px; letter-spacing: .2px;
  }
  .card--back { background: var(--olive); }
  .back__pattern {
    position: absolute; inset: 0;
    background: linear-gradient(135deg, var(--olive-light) 0%, var(--olive) 45%, var(--olive-deep) 100%);
  }
  .back__brand {
    position: absolute; right: 70px; bottom: 92px;
    color: var(--paper); font-weight: 700; font-size: 30px; letter-spacing: -.5px;
  }
</style>
</head>
<body>
<main class="stage">
  <section class="card card--front" aria-label="Business card front">
    <div class="front__brand">Brimovex</div>
    <div class="front__divider"></div>
    <div class="front__details">
      <div class="details__name">LEO MARWICK</div>
      <div class="details__title">President</div>
      <div class="details__address">1840 Harbor Crest Way<br>Seabrook CA 90412</div>
      <div class="contact">
        <svg viewBox="0 0 10 10" aria-hidden="true"><path d="M2 0.5 L3.8 2.6 L2.9 3.8 Q4 6 6.2 7.1 L7.4 6.2 L9.5 8 L8.3 9.5 Q1 8.5 0.5 1.7 Z"/></svg>
        <span>555-240-0187</span>
      </div>
      <div class="contact">
        <svg viewBox="0 0 10 10" aria-hidden="true"><path d="M0.5 2 H9.5 V8.5 H0.5 Z M1 2.5 L5 5.6 L9 2.5" stroke="#fff" stroke-width=".8"/></svg>
        <span>lmarwick@brimovex.com</span>
      </div>
      <div class="contact">
        <svg viewBox="0 0 10 10" aria-hidden="true"><circle cx="5" cy="5" r="4.5"/></svg>
        <span>www.brimovex.com</span>
      </div>
    </div>
    <p class="front__slogan">Your furry friends deserves the best</p>
  </section>

  <section class="card card--back" aria-label="Business card back">
    <div class="back__pattern" role="img" aria-label="Embossed repeating brand pattern in tone-on-tone olive"></div>
    <div class="back__brand">Brimovex</div>
  </section>
</main>
</body>
</html>
```